50th Anniversary Gala Save the date Postcard 8.5x5.5 inches

Looking for a 5.5x8.5 in one-sided postcard design for our annual gala. Design needs to include "Save the date" prominently with all the event information included below. Design should be light, include the colors of our logo and elegant. (almost like a wedding save the date). "Bridges of Grace" should look like its own logo.

50th Anniversary Gala at The Lodge at Birchmere Glen – “Bridges of Grace – Celebrating 50 Years of Building Community”
Thursday, October 24
6-11p
The Lodge at Birchmere Glen
Calloway Parkway, Ashbury Falls, VT
Honoring – TRB Previous Presidents

Target Market(s)

Exisiting donors

Industry/Entity Type

nonprofit

Font styles to use
Serif
Script

Requirements
Must have
• Save the date prominent
Should not have
• should not have a dark background

```html
<!DOCTYPE html>
<html lang="en">
<head>
<meta charset="utf-8">
<title>50th Anniversary Gala – Save the Date</title>
<link rel="stylesheet" href="https://fonts.googleapis.com/css2?family=Oswald:wght@700&family=Montserrat:wght@500;700;800&family=Merriweather:wght@400&family=Crimson+Pro:wght@500&display=swap">
<style>
  :root {
    --page-bg: #e9e9eb;
    --gold: #c9a13a;
    --ink: #2e2e33;
    --white: #ffffff;
    --blue: #1b7fd0;
    --blue-deep: #0f56a8;
    --navy: #183e7a;
    --green: #6db33f;
    --yellow: #fcd20a;
    --line: rgba(255,255,255,0.45);
  }
  * { margin: 0; padding: 0; box-sizing: border-box; }
  html, body { width: 1200px; height: 925px; overflow: hidden; background: var(--page-bg); }
  .postcard {
    position: absolute; left: 0; top: 67px;
    width: 1200px; height: 790px;
    background: var(--white); overflow: hidden;
  }
  .photo-area {
    position: absolute; left: 520px; top: 0; width: 680px; height: 560px;
    background: linear-gradient(90deg, rgba(255,255,255,1) 0%, rgba(236,226,212,0.6) 18%, #d9c7ae 45%, #b99a76 70%, #8f7a66 100%);
  }
  .waves { position: absolute; left: 0; top: 0; width: 1200px; height: 790px; }
  .headline {
    position: absolute; left: 54px; top: 52px;
    font-family: 'Oswald', sans-serif; font-weight: 700;
    font-size: 60px; line-height: 59px; color: var(--gold);
    letter-spacing: 0.5px;
  }
  .tagline {
    position: absolute; left: 56px; top: 250px;
    font-family: 'Montserrat', sans-serif; font-weight: 700;
    font-size: 24px; line-height: 36px; color: var(--ink);
  }
  .tagline .tagline-lead { font-size: 28px; }
  .save-badge {
    position: absolute; left: 488px; top: 321px; width: 186px; height: 186px;
    border-radius: 50%; background: radial-gradient(circle at 40% 35%, #ffffff 55%, #e3e3e6 100%);
    box-shadow: 0 4px 10px rgba(0,0,0,0.25), inset 0 0 0 4px #f4f4f6;
    display: flex; align-items: center; justify-content: center; text-align: center;
    font-family: 'Merriweather', serif; font-size: 38px; line-height: 37px; color: var(--ink);
  }
  .venue {
    position: absolute; left: 30px; top: 535px; width: 350px; text-align: center;
    font-family: 'Crimson Pro', serif; font-weight: 500; color: var(--white);
    font-size: 33px; line-height: 41px;
  }
  .venue .venue-label { margin-bottom: 8px; }
  .divider { position: absolute; left: 396px; top: 529px; width: 1px; height: 164px; background: var(--line); }
  .event-date {
    position: absolute; left: 406px; top: 521px; width: 350px; text-align: center;
    font-family: 'Montserrat', sans-serif; font-weight: 800; color: var(--white);
    font-size: 50px; line-height: 58px;
  }
  .org-seal {
    position: absolute; left: 758px; top: 366px; width: 382px; height: 382px; border-radius: 50%;
    background: radial-gradient(circle, #ffffff 78%, #dcdde1 92%, #f3f3f5 100%);
    box-shadow: 0 6px 14px rgba(0,0,0,0.25);
    display: flex; align-items: center; justify-content: center; text-align: center;
  }
  .org-name {
    font-family: 'Montserrat', sans-serif; font-weight: 700; font-size: 38px; line-height: 46px;
    color: var(--navy);
  }
  .honoring {
    position: absolute; left: 39px; top: 719px; width: 474px; height: 42px; border-radius: 8px;
    background: var(--navy); color: var(--white);
    font-family: 'Montserrat', sans-serif; font-weight: 500; font-size: 22px; line-height: 42px;
    padding-left: 17px;
  }
  .honoring strong { font-weight: 700; }
  .honoring-rule { position: absolute; left: 513px; top: 741px; width: 632px; height: 2px; background: var(--line); }
</style>
</head>
<body>
  <main class="postcard">
    <div class="photo-area" role="img" aria-label="Photo of smiling friends giving a high five around a table in a bright library"></div>

    <svg class="waves" viewBox="0 0 1200 790" aria-hidden="true">
      <defs>
        <linearGradient id="blueFill" x1="0" y1="0" x2="0" y2="1">
          <stop offset="0" stop-color="#2396dc"/>
          <stop offset="1" stop-color="#0f56a8"/>
        </linearGradient>
        <linearGradient id="yellowFade" x1="0" y1="0" x2="1" y2="0">
          <stop offset="0" stop-color="#fcd20a"/>
          <stop offset="0.55" stop-color="#fcd20a"/>
          <stop offset="0.85" stop-color="#fcd20a" stop-opacity="0"/>
        </linearGradient>
      </defs>
      <path d="M0,395 C200,365 420,360 700,380 L700,460 L0,500 Z" fill="url(#yellowFade)"/>
      <path d="M0,488 C250,430 560,400 840,408 C1000,414 1130,470 1200,560 L1200,790 L0,790 Z" fill="var(--green)"/>
      <path d="M0,502 C250,445 560,418 840,424 C1000,430 1130,500 1200,600 L1200,790 L0,790 Z" fill="url(#blueFill)"/>
    </svg>

    <h1 class="headline">50th ANNIVERSARY<br>GALA AT THE LODGE AT<br>BIRCHMERE GLEN</h1>
    <p class="tagline"><span class="tagline-lead">Bridges of Grace</span> - Celebrating<br>50 Years of Building Community</p>

    <div class="save-badge"><p>Save<br>the<br>Date</p></div>

    <div class="venue">
      <p class="venue-label">Venue:</p>
      <p>Calloway Parkway<br>Ashbury Falls, VT</p>
    </div>
    <div class="divider"></div>
    <p class="event-date">Thursday,<br>October 24.<br>6-11pm</p>

    <div class="org-seal"><p class="org-name">Kinship<br>Pathways</p></div>

    <p class="honoring"><strong>Honoring –</strong> TRB Previous Presidents</p>
    <div class="honoring-rule"></div>
  </main>
</body>
</html>
```